App Design

This is a 'video player' app - will be used to stream video files and watch them on a device. Need 3/4 skins for user customization.
Design will need to be versatile - used on: Veltrax4/4S/5 and zorBex2/3
Require an app design that shows the required functionality described by us, allows ease to navigate and visually creates a unique user experience.
App must have following pages: (refer to attached pages)
1. Search Page
2. Results Page
3. Video Page
4. End Page
3-4 skins for user preference
important: if you are interested please submit designs by tomorrow night - we will be picking from submitted designs - will make revisions and finalize the design within 4-5 days.
timing is crucial- please only submit if you can commit to timeline and design requirements. There will be refinements required.
Please see the attached update.
Additional reference files have been added to help in your efforts.
We have added a sample design that may help with your submissions. Please see brief
Project Deadline Extended
Project Deadline Extended
Project Deadline Extended
Target Market(s)
early adapters for technology / veltrax, tablet, quillon users
Requirements
Should not have
- should not be generic design

```html
<!DOCTYPE html>
<html lang="en">
<head>
<meta charset="utf-8">
<title>Video Player App – Screens</title>
<link href="https://fonts.googleapis.com/css2?family=Arimo:wght@400;700&family=Lobster&display=swap" rel="stylesheet">
<style>
  :root{
    --stage-top:#111a2c;
    --stage-mid:#34466c;
    --blue:#2a9be0;
    --blue-dark:#1a6fb4;
    --blue-light:#5cc2f5;
    --ink:#222;
    --muted:#555;
    --panel:#f3f3f3;
    --band:#dcdcdc;
    --bar-dark:#1e1e1e;
    --bar-mid:#3a3a3a;
    --pill:#b5b5b5;
    --check:#4dd12a;
    --overlay:rgba(22,30,38,.93);
    --photo-a:#9fb7c4;
    --photo-b:#2c3e4c;
  }
  *{box-sizing:border-box;margin:0;padding:0}
  html,body{width:1200px;height:1000px;overflow:hidden}
  body{
    background:radial-gradient(ellipse at 50% 75%,var(--stage-mid) 0%,var(--stage-top) 75%);
    font-family:"Arimo",Arial,sans-serif;
    position:relative;
  }
  .screen{position:absolute;top:192px;width:330px;height:590px;overflow:hidden;background:var(--panel)}
  .screen--feed{left:127px}
  .screen--settings{left:726px}

  .status-bar{position:absolute;left:0;top:0;width:100%;height:23px;background:#000;color:#fff;font-weight:700;font-size:14px;display:flex;align-items:center;padding:0 8px}
  .status-bar .signal{display:flex;align-items:flex-end;gap:1px;margin-right:4px}
  .status-bar .signal i{display:block;width:2px;background:#fff}
  .status-bar .carrier{letter-spacing:.2px}
  .status-bar .net{margin-left:9px}
  .status-bar .lock{position:absolute;left:158px;top:5px}
  .status-bar .battery{position:absolute;right:10px;top:7px;width:20px;height:9px;border:1px solid #fff;border-radius:2px;padding:1px}
  .status-bar .battery::after{content:"";display:block;width:100%;height:100%;background:#fff}

  .nav-bar{position:absolute;left:0;top:23px;width:100%;height:47px;background:linear-gradient(#45b1ee,var(--blue) 50%,var(--blue-dark));border-bottom:1px solid #0d4f86;text-align:center}
  .nav-title{font-family:"Lobster",cursive;color:#e9f4fb;font-size:27px;line-height:46px;text-shadow:0 2px 2px rgba(0,0,0,.35)}
  .toggle{position:absolute;display:flex;align-items:center;justify-content:space-between;background:linear-gradient(#2a2a2a,#555);border-radius:20px;box-shadow:inset 0 1px 3px rgba(0,0,0,.7)}
  .toggle .knob{border-radius:50%;background:radial-gradient(circle at 40% 35%,#fff,#cfcfcf);color:#999;font-size:8px;display:flex;align-items:center;justify-content:center}
  .nav-bar .toggle{right:7px;top:8px;width:60px;height:28px;padding:0 2px 0 6px}
  .nav-bar .toggle .knob{width:24px;height:24px}

  .search-band{position:absolute;left:0;top:70px;width:100%;height:43px;background:linear-gradient(#ececec,#d3d3d3)}
  .search-field{position:absolute;left:13px;top:8px;width:304px;height:25px;border:1px solid #a9a9a9;border-radius:4px;background:linear-gradient(#c9c9c9,#e0e0e0);font-size:10px;color:#444;display:flex;align-items:center;padding-left:8px;gap:10px}

  .photo{position:absolute;background:linear-gradient(160deg,var(--photo-a),#d8e3ea 45%,var(--photo-b))}
  .video-hero{left:0;top:114px;width:330px;height:200px}
  .icon-tile{position:absolute;width:33px;height:33px;border-radius:4px;background:var(--blue-light);display:flex;align-items:center;justify-content:center}
  .duration{position:absolute;right:8px;top:14px;background:var(--blue-light);color:#fff;font-size:10px;font-weight:700;padding:3px 4px;border-radius:3px}
  .play-btn{position:absolute;background:rgba(60,160,230,.75);border-radius:4px;display:flex;align-items:center;justify-content:center}
  .video-hero .play-btn{left:131px;top:66px;width:68px;height:68px}

  .video-info{position:absolute;left:0;top:314px;width:330px;height:119px;background:#f6f6f6;border-bottom:2px solid #bcbcbc}
  .author-thumb{left:7px;top:13px;width:38px;height:36px;background:linear-gradient(135deg,#8d8d8d,#3a3a3a)}
  .video-title{position:absolute;left:49px;top:13px;color:var(--blue);font-size:11px;font-weight:700}
  .byline{position:absolute;font-size:7px;font-weight:700;color:var(--ink)}
  .video-info .byline{left:49px;top:28px}
  .video-desc{position:absolute;left:8px;top:51px;width:316px;color:var(--blue);font-size:9px;line-height:11.5px}
  .stats{position:absolute;right:7px;top:87px;display:flex;gap:9px}
  .stat{height:18px;padding:0 6px;background:linear-gradient(#c6c6c6,#a2a2a2);border-radius:2px;font-size:7px;color:#222;display:flex;align-items:center;gap:5px}
  .feed-empty{position:absolute;left:0;top:435px;width:330px;height:103px;background:var(--band)}

  .tab-bar{position:absolute;left:0;top:538px;width:330px;height:52px;background:linear-gradient(var(--bar-mid),var(--bar-dark));display:flex}
  .tab{flex:1;display:flex;flex-direction:column;align-items:center;justify-content:flex-end;padding-bottom:6px;gap:6px;color:#cfcfcf;font-size:7px;font-weight:700;border-right:1px solid #111;border-left:1px solid #4a4a4a}
  .tab--active{background:linear-gradient(#6a6a6a,#3a3a3a);margin-top:-5px;border-radius:3px 3px 0 0}

  .grid-card{position:absolute;width:136px}
  .grid-card .photo{position:relative;width:136px;height:102px;border:3px solid #fff;box-shadow:0 1px 2px rgba(0,0,0,.4)}
  .grid-card .play-btn{left:52px;top:33px;width:30px;height:30px}
  .card-title{color:var(--blue);font-size:10px;font-weight:700;margin-top:6px;white-space:nowrap}
  .card-meta{display:flex;justify-content:space-between;font-size:6px;font-weight:700;color:#333;margin-top:3px}

  .settings-panel{position:absolute;left:5px;top:75px;width:320px;height:396px;background:var(--overlay);border:1px solid #3c6f97;box-shadow:0 3px 10px rgba(0,0,0,.5)}
  .settings-title{position:absolute;left:10px;top:10px;color:var(--blue);font-size:14px;font-weight:700}
  .settings-rule{position:absolute;left:10px;top:33px;width:300px;height:1px;background:var(--blue)}
  .close-btn{position:absolute;right:10px;top:8px;width:19px;height:19px;border-radius:50%;background:#fff;display:flex;align-items:center;justify-content:center}
  .settings-section{position:absolute;left:10px;color:var(--blue);font-size:12px;font-weight:700}
  .feature-row{position:absolute;left:10px;display:flex;align-items:center;gap:10px;color:var(--blue);font-size:9px}
  .feature-row .toggle{position:relative;width:38px;height:18px;padding:0 1px 0 3px}
  .feature-row .toggle .knob{width:16px;height:16px;font-size:6px}
</style>
</head>
<body>

<!-- Feed / video screen -->
<section class="screen screen--feed">
  <header class="status-bar">
    <span class="signal"><i style="height:3px"></i><i style="height:5px"></i><i style="height:7px"></i><i style="height:9px"></i><i style="height:11px"></i></span>
    <span class="carrier">VERIDA</span><span class="net">3G</span>
    <svg class="lock" width="10" height="12" viewBox="0 0 10 12"><path d="M2 5V3.5a3 3 0 0 1 6 0V5" fill="none" stroke="#fff" stroke-width="1.6"/><rect x="0.5" y="5" width="9" height="7" rx="1" fill="#fff"/></svg>
    <span class="battery"></span>
  </header>
  <div class="nav-bar">
    <span class="nav-title">Label</span>
    <div class="toggle">
      <svg width="18" height="16" viewBox="0 0 18 16"><path d="M2 8l5 5L16 2" fill="none" stroke="var(--check)" stroke-width="3.5" stroke-linecap="round" stroke-linejoin="round"/></svg>
      <span class="knob">‹ ›</span>
    </div>
  </div>
  <div class="search-band">
    <div class="search-field">
      <svg width="11" height="11" viewBox="0 0 12 12"><circle cx="5" cy="5" r="3.8" fill="none" stroke="#444" stroke-width="1.5"/><path d="M8 8l3.2 3.2" stroke="#444" stroke-width="1.7"/></svg>
      <span>Lorem Ipsum |</span>
    </div>
  </div>
  <div class="photo video-hero" role="img" aria-label="Video still: a man in a hat and coat standing by a railing in a bright blue-toned corridor">
    <span class="icon-tile" style="left:9px;top:14px">
      <svg width="20" height="18" viewBox="0 0 24 22"><path d="M12 21l-1.5-1.3C5 15 2 12 2 8.5 2 5.5 4.5 3 7.5 3c1.7 0 3.4.8 4.5 2.1C13.1 3.8 14.8 3 16.5 3 19.5 3 22 5.5 22 8.5c0 3.5-3 6.5-8.5 11.2z" fill="#fff"/></svg>
    </span>
    <span class="icon-tile" style="left:9px;top:65px">
      <svg width="22" height="18" viewBox="0 0 24 20"><ellipse cx="10" cy="8" rx="8" ry="6" fill="#fff"/><path d="M4 12l-2 5 6-3z" fill="#fff"/><ellipse cx="15" cy="11" rx="7" ry="5" fill="#fff" stroke="var(--blue-light)" stroke-width="1.2"/></svg>
    </span>
    <span class="duration">4.06</span>
    <span class="play-btn"><svg width="34" height="38" viewBox="0 0 34 38"><path d="M2 2l30 17L2 36z" fill="#fff"/></svg></span>
  </div>
  <article class="video-info">
    <div class="photo author-thumb" role="img" aria-label="Author avatar photo"></div>
    <h2 class="video-title">Lorem ipsum dolor</h2>
    <p class="byline">By Orvan</p>
    <p class="video-desc">Lorem ipsum dolor sit amet, consectetur adipisicing elit, sed do eiusmod tempor incididunt ut labore et dolore magna aliqua.</p>
    <div class="stats">
      <span class="stat"><svg width="10" height="9" viewBox="0 0 24 22"><path d="M12 21l-1.5-1.3C5 15 2 12 2 8.5 2 5.5 4.5 3 7.5 3c1.7 0 3.4.8 4.5 2.1C13.1 3.8 14.8 3 16.5 3 19.5 3 22 5.5 22 8.5c0 3.5-3 6.5-8.5 11.2z" fill="#333"/></svg>505,23</span>
      <span class="stat"><svg width="11" height="8" viewBox="0 0 22 14"><path d="M1 7C5 1 17 1 21 7 17 13 5 13 1 7z" fill="#333"/><circle cx="11" cy="7" r="3" fill="#bbb"/></svg>725,23</span>
      <span class="stat"><svg width="9" height="9" viewBox="0 0 10 10"><rect x="0.5" y="1.5" width="9" height="8" fill="none" stroke="#333"/><rect x="0.5" y="1.5" width="9" height="2.5" fill="#333"/></svg>12 June 2013</span>
    </div>
  </article>
  <div class="feed-empty"></div>
  <nav class="tab-bar">
    <div class="tab"><svg width="20" height="20" viewBox="0 0 20 20"><circle cx="10" cy="10" r="6.5" fill="none" stroke="#bbb" stroke-width="4" stroke-dasharray="3 2"/><circle cx="10" cy="10" r="5" fill="#bbb"/><circle cx="10" cy="10" r="2" fill="#2a2a2a"/></svg>Setting</div>
    <div class="tab"><svg width="24" height="16" viewBox="0 0 24 16"><path d="M1 8C6 1 18 1 23 8 18 15 6 15 1 8z" fill="#bbb"/><circle cx="12" cy="8" r="4" fill="#2a2a2a"/><circle cx="12" cy="8" r="2" fill="#bbb"/></svg>Recently Viewed</div>
    <div class="tab tab--active"><svg width="34" height="16" viewBox="0 0 34 16"><path d="M1 8C5 2 15 2 18 8 15 14 5 14 1 8z M16 8C19 2 29 2 33 8 29 14 19 14 16 8z" fill="#bbb"/><circle cx="10" cy="8" r="3" fill="#3a3a3a"/><circle cx="24" cy="8" r="3" fill="#3a3a3a"/></svg>Most Viewed</div>
    <div class="tab"><svg width="20" height="20" viewBox="0 0 20 20"><circle cx="8" cy="8" r="5.5" fill="none" stroke="#bbb" stroke-width="2"/><path d="M12 12l6 6" stroke="#bbb" stroke-width="3" stroke-linecap="round"/></svg>Search</div>
    <div class="tab"><svg width="22" height="20" viewBox="0 0 24 22"><path d="M12 21l-1.5-1.3C5 15 2 12 2 8.5 2 5.5 4.5 3 7.5 3c1.7 0 3.4.8 4.5 2.1C13.1 3.8 14.8 3 16.5 3 19.5 3 22 5.5 22 8.5c0 3.5-3 6.5-8.5 11.2z" fill="#bbb"/></svg>Favourites</div>
  </nav>
</section>

<!-- Settings overlay screen -->
<section class="screen screen--settings">
  <header class="status-bar">
    <span class="signal"><i style="height:3px"></i><i style="height:5px"></i><i style="height:7px"></i><i style="height:9px"></i><i style="height:11px"></i></span>
    <span class="carrier">VERIDA</span><span class="net">3G</span>
    <svg class="lock" width="10" height="12" viewBox="0 0 10 12"><path d="M2 5V3.5a3 3 0 0 1 6 0V5" fill="none" stroke="#fff" stroke-width="1.6"/><rect x="0.5" y="5" width="9" height="7" rx="1" fill="#fff"/></svg>
    <span class="battery"></span>
  </header>
  <div class="nav-bar">
    <span class="nav-title">App Name</span>
    <div class="toggle">
      <svg width="18" height="16" viewBox="0 0 18 16"><path d="M2 8l5 5L16 2" fill="none" stroke="var(--check)" stroke-width="3.5" stroke-linecap="round" stroke-linejoin="round"/></svg>
      <span class="knob">‹ ›</span>
    </div>
  </div>

  <div class="grid-card" style="left:16px;top:135px"><div class="photo" role="img" aria-label="Video thumbnail"><span class="play-btn"><svg width="14" height="16" viewBox="0 0 14 16"><path d="M1 1l12 7-12 7z" fill="#fff"/></svg></span></div><p class="card-title">Lorem Ipsum dolor ism....</p><p class="card-meta"><span>By Orvan</span><span>3 week ago</span></p></div>
  <div class="grid-card" style="left:176px;top:135px"><div class="photo" role="img" aria-label="Video thumbnail"><span class="play-btn"><svg width="14" height="16" viewBox="0 0 14 16"><path d="M1 1l12 7-12 7z" fill="#fff"/></svg></span></div><p class="card-title">Lorem Ipsum dolor ism....</p><p class="card-meta"><span>By Orvan</span><span>3 week ago</span></p></div>
  <div class="grid-card" style="left:16px;top:290px"><div class="photo" role="img" aria-label="Video thumbnail"><span class="play-btn"><svg width="14" height="16" viewBox="0 0 14 16"><path d="M1 1l12 7-12 7z" fill="#fff"/></svg></span></div><p class="card-title">Lorem Ipsum dolor ism....</p><p class="card-meta"><span>By Orvan</span><span>3 week ago</span></p></div>
  <div class="grid-card" style="left:176px;top:290px"><div class="photo" role="img" aria-label="Video thumbnail"><span class="play-btn"><svg width="14" height="16" viewBox="0 0 14 16"><path d="M1 1l12 7-12 7z" fill="#fff"/></svg></span></div><p class="card-title">Lorem Ipsum dolor ism....</p><p class="card-meta"><span>By Orvan</span><span>3 week ago</span></p></div>
  <div class="grid-card" style="left:16px;top:444px"><div class="photo" role="img" aria-label="Video thumbnail: a person standing in a dim blue room"><span class="play-btn"><svg width="14" height="16" viewBox="0 0 14 16"><path d="M1 1l12 7-12 7z" fill="#fff"/></svg></span></div><p class="card-title">Lorem Ipsum dolor ism....</p><p class="card-meta"><span>By Orvan</span><span>3 week ago</span></p></div>
  <div class="grid-card" style="left:176px;top:444px"><div class="photo" role="img" aria-label="Video thumbnail: a figure by a railing in a bright corridor"><span class="play-btn"><svg width="14" height="16" viewBox="0 0 14 16"><path d="M1 1l12 7-12 7z" fill="#fff"/></svg></span></div><p class="card-title">Lorem Ipsum dolor ism....</p><p class="card-meta"><span>By Orvan</span><span>3 week ago</span></p></div>

  <aside class="settings-panel">
    <h2 class="settings-title">Settings</h2>
    <span class="close-btn"><svg width="9" height="9" viewBox="0 0 9 9"><path d="M1 1l7 7M8 1L1 8" stroke="#222" stroke-width="2"/></svg></span>
    <span class="settings-rule"></span>
    <p class="settings-section" style="top:48px">Features</p>
    <div class="feature-row" style="top:73px">
      <div class="toggle"><svg width="12" height="11" viewBox="0 0 18 16"><path d="M2 8l5 5L16 2" fill="none" stroke="var(--check)" stroke-width="3.5" stroke-linecap="round" stroke-linejoin="round"/></svg><span class="knob">‹›</span></div>
      <span>Features 1</span>
    </div>
    <div class="feature-row" style="top:109px">
      <div class="toggle"><svg width="12" height="11" viewBox="0 0 18 16"><path d="M2 8l5 5L16 2" fill="none" stroke="var(--check)" stroke-width="3.5" stroke-linecap="round" stroke-linejoin="round"/></svg><span class="knob">‹›</span></div>
      <span>Features 2</span>
    </div>
    <p class="settings-section" style="top:163px">Help</p>
    <p class="settings-section" style="top:198px">About</p>
    <p class="settings-section" style="top:232px">Feedback</p>
    <p class="settings-section" style="top:265px">Privacy</p>
    <p class="settings-section" style="top:300px">Terms of Use</p>
  </aside>
</section>

</body>
</html>
```